Innovative Veterinary Clinic Business Card

We are a mixed animal veterinary practice in rural Queensland. Our patients include cattle, horses, dogs and cats, with everything in between. We are moving the clinic forward to become the best in our region and one of the best in the State, with gold standard service and standards of care, while remaining down to earth and genuine. Our current motto is - "The difference is, we care". The clinic colours are blue and red but am open to change. I would like something innovative and modern, that stands out and says we are different, we are amazing, and our patients come first. Something that will be remembered. Our current logo and business card I feel are empty and don't stand out.
Updates

please use font that is strong but simple. I am looking for something different, rather than your run of the mill business card. I am open to anything - as long as it has two sides and defines us, I'll consider all submissions. Thank you for your efforts, they are all very much appreciated!!

Thank you all very much for your amazing efforts. I wasn't expecting to have such a great response, so I thank you for your participation. You are all very talented and I loved your designs. I wish you all the best for the future. Thank you!

Target Market(s)

pet owners, graziers, horse clients (horses of all types - pets, campdrafting, mustering, polocrosse, thoroughbreds, show ponies)

Industry/Entity Type

Veterinary

Contact Information for Business Card

Dr. Petra L Hovland - BVSc (Hons)
Greenhollow Veterinary Services
18 Carrow St
Mundubbera, QLD, 4626
Ph: 0746382117 or 0418273946
Fax: 0746382110
e: greenhollowvet@mailbrook.net

Colors

Designer to choose colors to be used in the design.

Requirements
Must have
• back side of card to be used as an appointment card
Nice to have
• perhaps a photo of an animal (horse, dog, cat, cattle)
Should not have
• I don't want the standard name, rank and serial number business card. No cartoon animals.

```html
<!DOCTYPE html>
<html lang="en">
<head>
<meta charset="utf-8">
<title>Greenhollow Veterinary Services – Business Card</title>
<link rel="stylesheet" href="https://fonts.googleapis.com/css2?family=Cinzel:wght@400;600&family=Lato:wght@400;700&display=swap">
<style>
  :root {
    --navy: #1f3b4b;
    --gold: #a4946f;
    --ink: #2c3e4a;
    --paper: #ffffff;
    --backdrop: #e4e6e8;
    --rule: #b8ad93;
    --mist: #dcdde0;
  }
  * { box-sizing: border-box; margin: 0; padding: 0; }
  html, body { width: 1200px; height: 900px; overflow: hidden; }
  body {
    background: var(--backdrop);
    display: flex;
    flex-direction: column;
    align-items: center;
    justify-content: center;
    gap: 36px;
    font-family: "Lato", Arial, sans-serif;
    color: var(--ink);
  }
  .card {
    width: 700px;
    height: 400px;
    background: var(--paper);
    position: relative;
    overflow: hidden;
    box-shadow: 0 6px 18px rgba(0,0,0,0.18);
  }

  /* Appointment side */
  .appointment { padding: 46px 60px 0; }
  .appointment__scene {
    position: absolute;
    left: 150px; top: 20px;
    width: 470px; height: 300px;
    border-radius: 40% 40% 10px 10px;
    background: radial-gradient(ellipse at 45% 35%, var(--mist) 0%, rgba(220,221,224,0.55) 50%, rgba(255,255,255,0) 75%);
  }
  .appointment__content { position: relative; }
  .appointment__title {
    font-family: "Cinzel", Georgia, serif;
    font-weight: 400;
    font-size: 34px;
    letter-spacing: 2px;
    text-align: center;
    color: var(--navy);
    margin-bottom: 34px;
  }
  .appointment__field {
    display: flex;
    align-items: flex-end;
    gap: 14px;
    margin-bottom: 30px;
    font-size: 24px;
  }
  .appointment__label { color: var(--navy); white-space: nowrap; }
  .appointment__field--gold .appointment__label { color: var(--gold); }
  .appointment__line {
    flex: 1;
    border-bottom: 1.5px solid var(--navy);
    margin-bottom: 6px;
  }
  .appointment__field--gold .appointment__line { border-color: var(--rule); }
  .appointment__note {
    position: absolute;
    left: 0; right: 0;
    bottom: 38px;
    text-align: center;
    font-size: 15px;
    font-weight: 700;
    color: var(--gold);
  }
  .appointment__band {
    position: absolute;
    left: 0; right: 0; bottom: 0;
    height: 20px;
    background: var(--navy);
  }

  /* Contact side */
  .contact { display: flex; }
  .contact__brand {
    width: 51%;
    display: flex;
    align-items: center;
    justify-content: center;
    gap: 14px;
    padding: 0 30px;
  }
  .brand__square {
    width: 18px; height: 18px;
    background: var(--navy);
    flex-shrink: 0;
  }
  .brand__name {
    font-family: "Lato", Arial, sans-serif;
    font-weight: 700;
    font-size: 22px;
    line-height: 1.3;
    color: var(--navy);
  }
  .contact__details {
    width: 49%;
    background: var(--navy);
    color: var(--paper);
    padding: 36px 28px;
    display: flex;
    flex-direction: column;
  }
  .details__practice {
    font-size: 13px;
    font-weight: 700;
    color: var(--gold);
    white-space: nowrap;
    margin-bottom: 4px;
  }
  .details__address { font-size: 16px; line-height: 1.35; }
  .details__name {
    font-family: "Cinzel", Georgia, serif;
    font-size: 22px;
    color: var(--gold);
    margin-top: 42px;
  }
  .details__qual { font-size: 17px; margin-top: 4px; }
  .details__list { list-style: none; margin-top: auto; font-size: 16px; line-height: 1.6; }
  .details__key { color: var(--gold); font-weight: 700; margin-right: 4px; }
</style>
</head>
<body>

  <section class="card appointment" aria-label="Appointment card">
    <div class="appointment__scene" role="img" aria-label="Faint scene of a tree with a horse, dog, cat and bull"></div>
    <div class="appointment__content">
      <h2 class="appointment__title">APPOINTMENT</h2>
      <div class="appointment__field appointment__field--gold">
        <span class="appointment__label">Pet's Name:</span><span class="appointment__line"></span>
      </div>
      <div class="appointment__field">
        <span class="appointment__label">Date:</span><span class="appointment__line"></span>
      </div>
      <div class="appointment__field">
        <span class="appointment__label">Time:</span><span class="appointment__line"></span>
      </div>
    </div>
    <p class="appointment__note">Please let us know as soon as possible if you need to reschedule your appointment. Thank you.</p>
    <div class="appointment__band"></div>
  </section>

  <section class="card contact" aria-label="Contact card">
    <div class="contact__brand">
      <span class="brand__square"></span>
      <p class="brand__name">Greenhollow<br>Veterinary Services</p>
    </div>
    <div class="contact__details">
      <p class="details__practice">GREENHOLLOW VETERINARY SERVICES</p>
      <p class="details__address">18 Carrow Street Brackenvale,<br>QLD 4619</p>
      <p class="details__name">DR. PETRA L HOVLAND</p>
      <p class="details__qual">BVSc (Hons)</p>
      <ul class="details__list">
        <li><span class="details__key">P:</span>0746382117 / 0418273946</li>
        <li><span class="details__key">F:</span>0746382110</li>
        <li><span class="details__key">E:</span>greenhollowvet@mailbrook.net</li>
      </ul>
    </div>
  </section>

</body>
</html>
```